I am looking for business cards and letterhead

I want a high-level look for CEO's who want a concierge level leadership consultant and organization development strategist

This needs to go with my brand: simple, elegant, clean. Please improve on this design while using these fonts and colors

Here is my website: CorinneHalvers.com

```html
<!DOCTYPE html>
<html lang="en">
<head>
<meta charset="utf-8">
<title>Corinne Halvers — Business Card</title>
<link rel="stylesheet" href="https://fonts.googleapis.com/css2?family=Montserrat:wght@400;600;700&display=swap">
<style>
  :root {
    --navy: #0b1433;
    --gold: #c4a46c;
    --white: #ffffff;
    --backdrop: #ececec;
    --text-light: #ffffff;
  }
  * { margin: 0; padding: 0; box-sizing: border-box; }
  html, body {
    width: 1200px;
    height: 1200px;
    overflow: hidden;
    background: var(--backdrop);
    font-family: "Montserrat", Arial, sans-serif;
  }
  .canvas {
    position: relative;
    width: 1200px;
    height: 1200px;
  }
  .card {
    position: absolute;
    left: 178px;
    width: 845px;
    height: 496px;
    background: var(--white);
    overflow: hidden;
  }
  .card--front { top: 81px; }
  .card--back { top: 616px; }

  .band {
    position: absolute;
    top: 100px;
    height: 298px;
    background: var(--navy);
    border-top: 6px solid var(--gold);
    border-bottom: 7px solid var(--gold);
  }
  .band--main { left: 0; width: 533px; }
  .band--stub { left: 790px; width: 55px; }

  .holder-name {
    position: absolute;
    left: 50px;
    top: 150px;
    font-weight: 700;
    font-size: 37px;
    letter-spacing: 0.5px;
    color: var(--gold);
  }
  .contact-list {
    position: absolute;
    left: 50px;
    top: 238px;
    list-style: none;
  }
  .contact-item {
    display: flex;
    align-items: center;
    height: 39px;
    font-weight: 400;
    font-size: 22px;
    color: var(--text-light);
  }
  .contact-icon {
    width: 17px;
    height: 17px;
    margin-right: 15px;
    flex: none;
  }

  .brand-mark {
    position: absolute;
    display: flex;
    flex-direction: column;
    align-items: center;
    justify-content: center;
    color: var(--gold);
    font-weight: 600;
    text-align: center;
  }
  .brand-mark__circle {
    border: 3px solid var(--gold);
    border-radius: 50%;
  }
  .brand-mark--front {
    left: 549px;
    top: 146px;
    width: 225px;
    height: 210px;
    font-size: 21px;
  }
  .brand-mark--front .brand-mark__circle {
    width: 110px;
    height: 110px;
    margin-bottom: 16px;
  }
  .brand-mark--back {
    left: 222px;
    top: 96px;
    width: 400px;
    height: 300px;
    font-size: 30px;
  }
  .brand-mark--back .brand-mark__circle {
    width: 170px;
    height: 170px;
    margin-bottom: 24px;
  }
</style>
</head>
<body>
<main class="canvas">

  <section class="card card--front" aria-label="Business card front">
    <div class="band band--main"></div>
    <div class="band band--stub"></div>

    <h1 class="holder-name">YOUR NAME</h1>

    <ul class="contact-list">
      <li class="contact-item">
        <svg class="contact-icon" viewBox="0 0 24 24" aria-hidden="true">
          <path fill="#c4a46c" d="M6.6 10.8a15.1 15.1 0 0 0 6.6 6.6l2.2-2.2c.3-.3.7-.4 1-.2 1.1.4 2.3.6 3.6.6.6 0 1 .4 1 1V20c0 .6-.4 1-1 1A17 17 0 0 1 3 4c0-.6.4-1 1-1h3.5c.6 0 1 .4 1 1 0 1.3.2 2.5.6 3.6.1.3 0 .7-.2 1z"/>
        </svg>
        (512) 555 0147
      </li>
      <li class="contact-item">
        <svg class="contact-icon" viewBox="0 0 24 24" aria-hidden="true">
          <path fill="#c4a46c" d="M3 5h18a1 1 0 0 1 1 1v12a1 1 0 0 1-1 1H3a1 1 0 0 1-1-1V6a1 1 0 0 1 1-1zm9 7.5L20.5 7h-17z"/>
        </svg>
        info@CorinneHalvers.com
      </li>
      <li class="contact-item">
        <svg class="contact-icon" viewBox="0 0 24 24" aria-hidden="true">
          <circle cx="12" cy="12" r="9.5" fill="none" stroke="#c4a46c" stroke-width="2"/>
          <ellipse cx="12" cy="12" rx="4" ry="9.5" fill="none" stroke="#c4a46c" stroke-width="1.6"/>
          <line x1="2.5" y1="12" x2="21.5" y2="12" stroke="#c4a46c" stroke-width="1.6"/>
        </svg>
        www.CorinneHalvers.com
      </li>
    </ul>

    <div class="brand-mark brand-mark--front">
      <span class="brand-mark__circle"></span>
      <span class="brand-mark__name">Corinne Halvers</span>
    </div>
  </section>

  <section class="card card--back" aria-label="Business card back">
    <div class="brand-mark brand-mark--back">
      <span class="brand-mark__circle"></span>
      <span class="brand-mark__name">Corinne Halvers</span>
    </div>
  </section>

</main>
</body>
</html>
```